New Wordpress Design Project (Torvak)

We need a wordpress design for an established auction and real estate company based in Ohio. The winning design will incorporate highlight colors of logo (green white and yellow) creatively in a very professional and clean layout. Client mentions liking the site http://www.brindlepeakbids.example for use of color and layout, and http://www.quillmoreauctioneers.example/ as a general idea for what they like.
Updates

Designers - please note that this website will be built on a responsive theme so consideration should be given to the layout elements associated with the design, in particular the slideshow.  Thanks much and please post any questions that you have regarding this.

designs@lotmarkhub.example

Industry/Entity Type

Real Estate

Requirements
Must have
• navigation:
1) Home
2) Upcoming Auctions
3) Online Auctions
4) Real Estate
5) Services
6) About Us
7) Auction Gallery
8) Contact

Header will have logo and a slideshow element; please use stock real estate image to reflect the slideshow layout. Use horizontal navigation.
Sidebar widgets: email signup form, video widget, Upcoming Auction Widget, News blog, social media icons for facebook youtube and RSS, a button to "Register Now"
Footer will have smaller logo, small navigation, and 2 attached logos.
Nice to have
• drop down menu sample
Should not have
• no gavels in design

```html
<!DOCTYPE html>
<html lang="en">
<head>
<meta charset="utf-8">
<title>Don Torvak Auctions &amp; Real Estate</title>
<link rel="stylesheet" href="https://fonts.googleapis.com/css2?family=Didact+Gothic&family=Arimo:ital,wght@0,400;0,700;1,400;1,700&display=swap">
<style>
:root{
  --green:#0b7a3b;
  --green-dark:#06622e;
  --yellow:#f2e11a;
  --ink:#222;
  --line:#d8d8d8;
  --hero-a:#c9d3dc;
  --hero-b:#e6ebef;
}
*{box-sizing:border-box;margin:0;padding:0}
html,body{width:976px;height:1200px;overflow:hidden}
body{position:relative;background:#fff;font-family:"Arimo",Arial,sans-serif;color:var(--ink)}
.abs{position:absolute}
.display{font-family:"Didact Gothic","Century Gothic",sans-serif;font-weight:400}

/* header */
.site-header{left:0;top:0;width:976px;height:118px;background:linear-gradient(#fff,#f1f1f1)}
.brand{left:83px;top:20px;width:145px;height:84px;display:flex;align-items:center;gap:7px}
.brand-mark{width:16px;height:16px;background:var(--yellow);flex:none}
.brand-name{font-family:"Didact Gothic",sans-serif;font-size:15px;line-height:1.2;color:var(--green)}
.call{left:707px;top:33px;font-weight:700;font-size:18px;color:var(--green)}
.nav-home{left:257px;top:72px;width:37px;height:32px;background:var(--green)}
.main-nav{left:0;top:80px;font-family:"Didact Gothic",sans-serif;font-size:12.5px;color:#222}
.main-nav span{position:absolute;white-space:nowrap}

/* hero */
.hero{left:0;top:119px;width:976px;height:302px;background:linear-gradient(90deg,var(--hero-a),var(--hero-b) 50%,var(--hero-a))}
.slide{left:112px;top:131px;width:421px;height:269px;background:radial-gradient(ellipse at 50% 55%,#cfc8c0,#a79a8e 60%,#7d6f64)}
.slide-caption{left:112px;top:360px;width:421px;height:40px;background:rgba(70,70,70,.55);color:#1b1b1b;font-size:10.5px;padding:11px 7px;white-space:nowrap}
.signup{left:545px;top:131px;width:255px;height:269px;background:#fff}
.signup h2{position:absolute;left:19px;top:9px;font-size:22px;color:var(--green);white-space:nowrap}
.signup label{position:absolute;left:10px;font-size:8px;line-height:10px;color:#222}
.signup .field{position:absolute;left:73px;width:168px;height:24px;border-radius:12px;background:linear-gradient(#e6e6e6,#f7f7f7);border:1px solid #e0e0e0}
.signup .btn{position:absolute;left:66px;top:237px;width:93px;height:32px;border-radius:46px 46px 0 0;background:linear-gradient(#2aa35a,var(--green-dark));color:#fff;font-family:"Didact Gothic",sans-serif;font-size:15px;text-align:center;padding-top:8px}

/* updates */
.band-fade{left:0;top:421px;width:976px;height:81px;background:linear-gradient(#fff,#f0f0f0)}
.updates{left:94px;top:443px;width:785px;height:43px;background:#f5f5f5;border:1px solid #e0e0e0;border-radius:3px}
.updates-tag{left:103px;top:449px;height:30px;width:60px;background:var(--green);color:#fff;font-weight:700;font-size:11px;padding:8px 0 0 10px}
.updates-text{left:182px;top:460px;font-size:10px;color:#222;white-space:nowrap}

/* welcome */
.welcome-title{left:82px;top:522px;font-size:18.5px;color:#1a1a1a;white-space:nowrap}
.welcome-text{left:83px;top:546px;width:528px;font-size:10.2px;line-height:16.3px;text-align:justify}
.read-more{left:543px;top:595px;font-size:10.5px;font-weight:700;color:var(--green)}

.post{left:88px;top:631px;width:500px;height:247px;border:1px solid var(--line);background:#fff}
.post-photo{left:107px;top:681px;width:169px;height:168px;border:4px solid #ddd;background:linear-gradient(#a9c3dc 0,#bfcfdc 40%,#8a5a48 55%,#6e8a4e 85%)}
.post-meta{left:289px;top:678px;width:268px;height:41px;background:#ececec;font-size:9.5px;line-height:17px;color:#888;padding:3px 8px}
.post-meta b{color:#666}
.post-text{left:289px;top:728px;width:281px;font-size:9.8px;line-height:17px;color:#888}
.post-btn{left:289px;top:839px;width:137px;height:23px;border:1px solid #ccc;border-radius:3px;background:linear-gradient(#fff,#eee);font-size:9.5px;color:#444;padding:5px 0 0 11px;white-space:nowrap}

/* upcoming */
.upcoming-title{left:83px;top:903px;font-size:23px;color:#1a1a1a;letter-spacing:.5px;white-space:nowrap}
.upcoming-sub{left:88px;top:939px;font-size:12px;font-weight:700;color:var(--green);white-space:nowrap}
.auction-photo{left:84px;top:963px;width:114px;height:76px;background:linear-gradient(#a9c9e8,#8fb07a 55%,#5f8a3c)}
.auction-info{left:206px;top:981px;font-size:10px;font-style:italic;line-height:11.5px;color:#222}
.auction-links{left:525px;top:961px;width:124px;height:75px;background:#f0f0f0;border:1px solid var(--line);font-size:11px;font-weight:700;color:#222}
.auction-links div{position:absolute;left:5px;right:5px;display:flex;align-items:center;gap:7px;white-space:nowrap}

/* sidebar */
.search{left:652px;top:526px;width:213px;height:25px;border:1px solid #ddd;background:#f4f4f4;font-size:9.5px;color:#666;padding:7px 4px}
.side-h{left:653px;top:560px;font-size:11.5px;color:var(--green)}
.side-p{left:653px;top:576px;font-size:9.5px;color:#777}
.social-sq{top:594px;width:16px;height:16px;border-radius:3px}
.featured{left:651px;top:642px;font-size:23px;color:#333;letter-spacing:.5px;white-space:nowrap}
.video{left:649px;top:685px;width:134px;height:101px;background:linear-gradient(120deg,#d8e6f2,#9fb7cc 55%,#5d6b78)}
.video-date{left:783px;top:711px;font-size:16px;color:#aaa;white-space:nowrap}
.video-caption{left:785px;top:734px;font-size:12px;color:#aaa}
.news{left:653px;top:842px;width:237px;height:190px;border:1px solid #e3e3e3;border-radius:6px;background:linear-gradient(#f3f3f3,#fff 30%)}
.news h3{position:absolute;left:20px;top:7px;font-size:21px;color:#333;letter-spacing:.5px;white-space:nowrap}
.news-thumb{width:42px;height:41px;background:linear-gradient(#7a5a44,#c9a58a)}
.news-item{font-size:9px;line-height:11.3px;font-style:italic;color:#333}
.news-item b{font-style:normal;color:var(--green)}
.news-date{font-size:9.5px;font-weight:700;font-style:italic;color:#222}

/* footer */
.site-footer{left:0;top:1058px;width:976px;height:142px;background:var(--green)}
.foot-brand{left:94px;top:1080px;display:flex;align-items:center;gap:6px}
.foot-brand .brand-mark{background:#fff}
.foot-brand span{font-family:"Didact Gothic",sans-serif;font-size:14px;line-height:1.2;color:#fff}
.badge{border:2px solid #fff}
.foot-nav{left:84px;top:1153px;font-size:10px;color:#fff;word-spacing:1px;white-space:nowrap}
.copy{left:84px;top:1171px;font-size:10px;color:#fff}
.foot-circle{top:1147px;width:36px;height:36px;border-radius:50%}
</style>
</head>
<body>

<header class="site-header abs"></header>
<div class="brand abs"><span class="brand-mark"></span><span class="brand-name">Don Torvak Auctions &amp; Real Estate</span></div>
<div class="call abs">Call Us:(123)-456-789</div>
<div class="nav-home abs">
  <svg width="37" height="32" viewBox="0 0 37 32"><path d="M18.5 8 L10 15.5 H12.5 V23 H16.5 V18.5 H20.5 V23 H24.5 V15.5 H27 Z" fill="#fff"/></svg>
</div>
<nav class="main-nav abs">
  <span style="left:305px">Upcoming Auctions</span>
  <span style="left:450px">Online Auctions</span>
  <span style="left:564px">Real Estate</span>
  <span style="left:652px">Services</span>
  <span style="left:723px">About Us</span>
  <span style="left:799px">Auction Gallery</span>
  <span style="left:912px">Contact</span>
</nav>

<section class="hero abs"></section>
<div class="slide abs" role="img" aria-label="Stock photo of two hands holding a small model house"></div>
<div class="slide-caption abs">Real Estate Alternatives: A Real Estate Investment Program For Beginners</div>

<form class="signup abs">
  <h2 class="display">Email Sign Up Form</h2>
  <label style="top:49px">First Name :</label><span class="field" style="top:44px"></span>
  <label style="top:88px">Last Name :</label><span class="field" style="top:83px"></span>
  <label style="top:126px">First Name :</label><span class="field" style="top:121px"></span>
  <label style="top:166px">Last Name :</label><span class="field" style="top:161px"></span>
  <span class="btn">Sign Up</span>
</form>

<div class="band-fade abs"></div>
<div class="updates abs"></div>
<div class="updates-tag abs">Updates</div>
<svg class="abs" style="left:162px;top:449px" width="14" height="34" viewBox="0 0 14 34"><path d="M0 0 L14 17 L0 34 Z" fill="#0b7a3b"/></svg>
<div class="updates-text abs">Learnvale was established taking forward the vision of few IITians who were mesmerized with the use of technology in the field of education in Singapore.</div>

<h1 class="welcome-title abs display">Welcome to Don Torvak Auctions &amp; Real Estate</h1>
<p class="welcome-text abs">simply dummy text of the printing and typesetting industry. Lorem Ipsum has been the industry's standard dummy text ever since the 1500s, when an unknown printer took a galley of type and scrambled it to make a type speci men book. It has survived not only five centuries, but also a galley of type and scrambled &nbsp;the leap into electronic typesetting,</p>
<a class="read-more abs">read more &gt;&gt;</a>

<article class="post abs"></article>
<div class="post-photo abs" role="img" aria-label="Photo of a brick two-storey house with lawn"></div>
<div class="post-meta abs">On 05.30.12 • In <b>Web Design Concepts</b>, <b>Web Design Guides</b>, <b>Web Design Tips</b> • by <b>Rena</b></div>
<p class="post-text abs">Everything is this world keeps changing and same rule applies to the website designing. Latest trends and designs keep on emerging. Therefore, website designers should change their designing style from time to time, so that they can keep up with the changing trends. Website designing field is very dynamic in nature, it keeps on changing [...]</p>
<div class="post-btn abs">Leave Your <b>Comments</b> »</div>

<h2 class="upcoming-title abs display">Upcoming Auctions</h2>
<div class="upcoming-sub abs">Incredible Home in Pine Hollow's exclusive Cedar Ridge community</div>
<div class="auction-photo abs" role="img" aria-label="Photo of a home with palm trees and lawn"></div>
<div class="auction-info abs">
  <b>Begins:</b> &nbsp;Tuesday, April 23, 2013 at 10:00 AM EDT<br><br>
  <b>Location:</b> &nbsp;Cedar Ridge Entrance- 1840 N. Harbor Hwy 17<br>
  Cedar Ridge Rd (Auction Property)<br>
  Pine Hollow, FL 33999
</div>
<div class="auction-links abs">
  <div style="top:10px"><svg width="20" height="18" viewBox="0 0 20 18"><rect x="1" y="1" width="18" height="16" fill="#fff" stroke="#5a7fa8"/><path d="M4 5h12M4 9h12M4 13h12" stroke="#5a7fa8"/></svg>Details</div>
  <div style="top:38px;border-top:1px solid #ddd;padding-top:9px"><svg width="20" height="18" viewBox="0 0 20 18"><rect x="1" y="4" width="18" height="13" rx="2" fill="#34506e"/><circle cx="10" cy="10.5" r="4" fill="#9fc0de"/></svg>Photo Galleries</div>
</div>

<div class="search abs">Search...</div>
<svg class="abs" style="left:874px;top:530px" width="18" height="18" viewBox="0 0 18 18"><circle cx="7" cy="7" r="5" fill="none" stroke="#777" stroke-width="2"/><path d="M11 11 L16 16" stroke="#555" stroke-width="3"/></svg>
<div class="side-h abs display">Social Media Icons</div>
<div class="side-p abs">simply dummy text of the printing</div>
<span class="social-sq abs" style="left:653px;background:#e0702a"></span>
<span class="social-sq abs" style="left:676px;background:#3d5e99"></span>
<span class="social-sq abs" style="left:699px;background:#4aa6cf"></span>
<span class="social-sq abs" style="left:722px;background:#2f6f9e"></span>
<span class="social-sq abs" style="left:745px;background:#c9281d"></span>

<h2 class="featured abs display">Featured Vedios</h2>
<div class="video abs" role="img" aria-label="Featured video thumbnail"></div>
<div class="video-date abs display">10 May 2013</div>
<div class="video-caption abs display">Lorem ipsum</div>

<aside class="news abs"><h3 class="display">News &amp; Events</h3></aside>
<div class="news-thumb abs" style="left:667px;top:888px" role="img" aria-label="Portrait thumbnail"></div>
<div class="news-item abs" style="left:711px;top:889px;width:180px"><b>simply dummy text of the</b><br>printing and typesetting industry. Lorem Ipsum has been the industry's.</div>
<div class="news-date abs" style="left:805px;top:929px">January 12, 2013</div>
<div class="news-thumb abs" style="left:667px;top:967px" role="img" aria-label="Portrait thumbnail"></div>
<div class="news-item abs" style="left:715px;top:968px;width:174px"><b>simply dummy text of the</b><br>printing and typesetting industry. Lorem Ipsum has been the industry's.</div>
<div class="news-date abs" style="left:807px;top:1008px">January 12, 2013</div>

<footer class="site-footer abs"></footer>
<div class="foot-brand abs"><span class="brand-mark"></span><span>Don Torvak Auctions<br>&amp; Real Estate</span></div>
<span class="badge abs" style="left:246px;top:1088px;width:37px;height:41px"></span>
<span class="badge abs" style="left:298px;top:1090px;width:45px;height:40px;border-radius:50%"></span>
<div class="foot-nav abs">Home &nbsp;| &nbsp;Upcoming Auctions &nbsp;| &nbsp;Online Auctions &nbsp;| &nbsp;Real Estate &nbsp;| &nbsp;Services &nbsp;| &nbsp;About Us &nbsp;| &nbsp;Auction Gallery &nbsp;| &nbsp;Contact</div>
<div class="copy abs">Copyright © 2013 - 2013 Don Torvak Auctioneers. All Rights Reserved</div>
<span class="foot-circle abs" style="left:676px;background:#1f4f8a"></span>
<span class="foot-circle abs" style="left:721px;background:#2a9ad8"></span>
<span class="foot-circle abs" style="left:766px;background:#f08a1c"></span>
<span class="foot-circle abs" style="left:810px;background:#bdbdbd"></span>
<svg class="abs" style="left:819px;top:1159px" width="18" height="12" viewBox="0 0 18 12"><rect x=".5" y=".5" width="17" height="11" fill="none" stroke="#fff"/><path d="M.5 .5 L9 7 L17.5 .5" fill="none" stroke="#fff"/></svg>

</body>
</html>
```